Website for Apartment Rental in Prague

I would like to create designs of my website focused on luxury apartment rentals in Prague, Czech Republic. I created initial mock-ups, They are all attached. I need to design homepage and subpage. The mock-ups were created by combining elements from different websites that I liked but I need you to create a design that is unique and original. The attached files a only a guidance for the structure of the website but not for the design. Try to be creative.

Industry/Entity Type

Apartment

```html
<!DOCTYPE html>
<html lang="en">
<head>
<meta charset="utf-8">
<title>Lumen Apartments Prague – Being Home in Prague</title>
<link href="https://fonts.googleapis.com/css2?family=Montserrat:wght@400;500;600;700&family=Cormorant+Garamond:ital,wght@1,500;1,600&family=Open+Sans:wght@400;600;700&display=swap" rel="stylesheet">
<style>
:root{
  --navy:#0c1120;
  --navy-deep:#070a14;
  --gold:#c9a54b;
  --gold-soft:#d8b96a;
  --ribbon:#f6c21c;
  --ink:#1d1d1d;
  --muted:#6c6c6c;
  --paper:#ffffff;
  --mist:#f8f8f8;
  --line:#e4e0d4;
}
*{box-sizing:border-box;margin:0;padding:0}
html,body{width:1200px;height:3782px;overflow:hidden}
body{background:var(--paper);font-family:'Montserrat',sans-serif;color:var(--ink);position:relative}
.abs{position:absolute}

/* top bar */
.topbar{position:absolute;left:0;top:0;width:1200px;height:40px;background:var(--navy);color:#fff;font-size:10px;font-weight:700;letter-spacing:.5px}
.topbar span{position:absolute;top:14px;white-space:nowrap}

/* navigation */
.nav{position:absolute;left:0;top:40px;width:1200px;height:98px;background:#fff;font-size:10px;font-weight:600;letter-spacing:.6px;color:var(--ink)}
.nav a{position:absolute;top:47px;color:inherit;text-decoration:none;text-transform:uppercase;white-space:nowrap}
.brand{position:absolute;left:520px;top:24px;width:160px;text-align:center;font-weight:700;font-size:14px;letter-spacing:3px;color:var(--ink);line-height:22px}
.brand small{display:block;font-size:14px}

/* hero */
.hero{position:absolute;left:0;top:138px;width:1200px;height:462px}
.hero-photo{position:absolute;left:0;top:0;width:1200px;height:437px;background:linear-gradient(90deg,#4a3f36 0%,#8c7a67 18%,#c9b8a1 40%,#e8ddc8 58%,#b49f83 78%,#5a4c40 100%)}
.hero-base{position:absolute;left:0;top:437px;width:1200px;height:25px;background:var(--navy)}
.hero-title{position:absolute;left:0;top:150px;width:1200px;text-align:center;color:#fff;font-weight:700;font-size:50px;letter-spacing:4px}
.booking{position:absolute;left:68px;top:328px;width:1096px;height:134px;background:#fff}
.field{position:absolute;top:50px;height:32px;border-bottom:1px solid var(--line);color:var(--gold);font-size:10px;font-weight:600;letter-spacing:1.2px}
.field span{position:absolute;left:0;top:10px;white-space:nowrap}
.field svg{position:absolute;right:0;top:13px}
.search-btn{position:absolute;left:809px;top:46px;width:34px;height:34px;background:var(--navy)}
.divider{position:absolute;left:870px;top:32px;width:1px;height:70px;background:var(--line)}

/* vision */
.vision{position:absolute;left:0;top:600px;width:1200px;height:363px;background:var(--navy)}
.script{font-family:'Cormorant Garamond',serif;font-style:italic;font-weight:500;text-align:center}
.vision .script{position:absolute;left:0;top:72px;width:1200px;font-size:34px;color:#5f6170}
.kicker{text-align:center;color:var(--gold);font-size:16px;font-weight:500;letter-spacing:7px}
.vision .kicker{position:absolute;left:0;top:121px;width:1200px}
.vision p{position:absolute;left:150px;top:170px;width:900px;text-align:center;font-family:'Open Sans',sans-serif;font-size:11px;line-height:20px;color:#6a6d7a}
.btn-outline-gold{position:absolute;left:520px;top:250px;width:160px;height:38px;border:1px solid var(--gold);color:var(--gold);font-size:10px;letter-spacing:2px;text-align:center;line-height:36px;font-weight:600}

/* listings */
.listings{position:absolute;left:0;top:963px;width:1200px;height:990px;background:var(--mist)}
.card{position:absolute;width:325px;height:411px;background:#fff;overflow:hidden}
.card-photo{position:absolute;left:0;top:0;width:325px;height:283px}
.photo-a{background:linear-gradient(160deg,#dcd6cc 0%,#c7bfb2 45%,#7e7468 75%,#4a4640 100%)}
.photo-b{background:linear-gradient(160deg,#f2f0ec 0%,#e0ddd7 50%,#9c968e 80%,#5e5a55 100%)}
.photo-c{background:linear-gradient(160deg,#ede9e0 0%,#d6cdbd 45%,#8d8273 78%,#4f483f 100%)}
.price{position:absolute;left:20px;top:172px;color:#fff;font-size:26px;font-weight:700;font-family:'Open Sans',sans-serif;line-height:34px}
.card-title{position:absolute;left:20px;top:208px;color:#fff;font-size:12px;font-weight:700;font-family:'Open Sans',sans-serif;line-height:20px;white-space:nowrap}
.stars{position:absolute;left:20px;top:258px}
.card-text{position:absolute;left:20px;top:296px;width:285px;font-family:'Open Sans',sans-serif;font-size:11px;line-height:20px;color:#333}
.card-meta{position:absolute;left:20px;top:334px;font-family:'Open Sans',sans-serif;font-size:11px;font-weight:700;color:#222;white-space:nowrap}
.btn-fill{position:absolute;left:20px;top:368px;width:138px;height:40px;background:var(--gold);color:#fff;font-size:10px;letter-spacing:2px;text-align:center;line-height:40px;font-weight:600}
.btn-line{position:absolute;left:166px;top:368px;width:139px;height:40px;border:1px solid var(--gold-soft);color:var(--gold);font-size:10px;letter-spacing:2px;text-align:center;line-height:38px;font-weight:600}
.ribbon{position:absolute;left:-40px;top:30px;width:190px;height:38px;background:var(--ribbon);color:#fff;transform:rotate(-45deg);text-align:center;line-height:38px;font-family:'Open Sans',sans-serif;font-weight:700;font-size:14px}

/* interior */
.section-title{position:absolute;left:0;width:1200px;font-size:32px;color:var(--ink)}
.interior-text{position:absolute;left:165px;top:2072px;width:870px;text-align:center;font-family:'Open Sans',sans-serif;font-size:11px;line-height:22px;color:#222}
.tile{position:absolute}
.zoom{position:absolute;width:52px;height:52px;border-radius:50%;background:#fff}

/* reminders */
.reminder{position:absolute;top:3062px;width:240px;text-align:center}
.reminder p{margin-top:16px;font-family:'Open Sans',sans-serif;font-size:11px;line-height:20px;color:var(--gold)}

/* footer */
.footer{position:absolute;left:0;top:3302px;width:1200px;height:408px;background:var(--navy)}
.footer h4{position:absolute;top:88px;color:var(--gold);font-size:14px;font-weight:700;letter-spacing:2px;white-space:nowrap}
.about{position:absolute;left:86px;top:128px;width:242px;font-family:'Open Sans',sans-serif;font-size:12px;line-height:19px;color:#c9cbd3}
.read-more{position:absolute;left:86px;top:206px;color:var(--gold);font-family:'Open Sans',sans-serif;font-size:12px}
.links{position:absolute;left:362px;top:124px;list-style:none;font-family:'Open Sans',sans-serif;font-size:12px;color:#fff;line-height:20px}
.links li{height:35px}
.links li.active{color:var(--gold)}
.news{position:absolute;left:612px;width:240px;height:80px;font-family:'Open Sans',sans-serif;font-size:12px;color:#fff;line-height:19px}
.news .thumb{position:absolute;left:0;top:4px;width:44px;height:44px}
.news .body{position:absolute;left:62px;top:0;width:178px}
.news .body b{font-weight:600;letter-spacing:.5px;font-size:11px}
.newsletter{position:absolute;left:912px;top:124px;width:200px;height:38px;background:#fff}
.newsletter span{position:absolute;left:16px;top:11px;font-family:'Open Sans',sans-serif;font-size:12px;color:#888}
.newsletter i{position:absolute;right:0;top:0;width:36px;height:38px;background:var(--gold)}
.social-dot{position:absolute;top:238px;width:24px;height:24px;border-radius:50%;background:#fff}
.bottom-bar{position:absolute;left:0;top:3710px;width:1200px;height:72px;background:var(--navy-deep);color:#fff;font-family:'Open Sans',sans-serif;font-size:12px;text-align:center;line-height:64px}
</style>
</head>
<body>

<header class="topbar">
  <span style="left:83px">DISCOVER PRAGUE</span>
  <span style="left:227px">OUR HOSPITALITY</span>
  <span style="left:363px">EN</span>
  <span style="left:752px">RESERVATION@LUMENSTAY.CZ</span>
  <span style="left:1008px">+420 600 100 200</span>
</header>

<nav class="nav">
  <a style="left:83px">Appartments</a>
  <a style="left:200px">Location</a>
  <a style="left:290px">Services</a>
  <a style="left:375px">Gallery</a>
  <a style="left:455px">News</a>
  <div class="brand">LUMEN<small>PRAGUE</small></div>
  <a style="left:698px">Exclusive Offers and Tours</a>
  <a style="left:920px">For Families</a>
  <a style="left:1032px">Contact Us</a>
</nav>

<section class="hero">
  <div class="hero-photo" role="img" aria-label="Photo of a bright apartment bedroom with curtains and a made bed"></div>
  <div class="hero-base"></div>
  <h1 class="hero-title">BEING HOME IN PRAGUE</h1>
  <form class="booking">
    <div class="field" style="left:28px;width:176px"><span>SELECT DATES</span>
      <svg width="14" height="13" viewBox="0 0 14 13"><rect x="1" y="2" width="12" height="10" fill="none" stroke="#c9a54b"/><line x1="1" y1="5" x2="13" y2="5" stroke="#c9a54b"/></svg></div>
    <div class="field" style="left:237px;width:104px"><span>ADULTS</span>
      <svg width="8" height="5"><path d="M0 0h8L4 5z" fill="#c9a54b"/></svg></div>
    <div class="field" style="left:368px;width:106px"><span>CHILDREN</span>
      <svg width="8" height="5"><path d="M0 0h8L4 5z" fill="#c9a54b"/></svg></div>
    <div class="field" style="left:502px;width:106px"><span>INFANTS</span>
      <svg width="8" height="5"><path d="M0 0h8L4 5z" fill="#c9a54b"/></svg></div>
    <div class="field" style="left:630px;width:154px"><span>PROMO CODE</span></div>
    <div class="search-btn">
      <svg width="34" height="34" viewBox="0 0 34 34"><circle cx="16" cy="16" r="5" fill="none" stroke="#fff" stroke-width="2"/><line x1="19.5" y1="19.5" x2="23" y2="23" stroke="#fff" stroke-width="2"/></svg>
    </div>
    <div class="divider"></div>
    <div class="field" style="left:895px;width:152px"><span>RENTAL UNIT</span>
      <svg width="8" height="5"><path d="M0 0h8L4 5z" fill="#c9a54b"/></svg></div>
  </form>
</section>

<section class="vision">
  <h2 class="script">A Different Vision of</h2>
  <div class="kicker">TRAVELING</div>
  <p>Something spectacular has arrived in the heart of Europe. Steps from Old town, this rental experience is curated with world class amenities, exemplary style and a level of convenience you have to experience to believe. Experience is the different vision of luxury in the center of Prague</p>
  <div class="btn-outline-gold">LEARN MORE</div>
</section>

<section class="listings">
  <svg width="0" height="0" style="position:absolute"><defs><path id="st" d="M7 0l2 5h5l-4 3 1.6 5L7 10l-4.6 3L4 8 0 5h5z" fill="#c9a54b"/></defs></svg>

  <article class="card" style="left:86px;top:50px">
    <div class="card-photo photo-a" role="img" aria-label="Photo of a bright living room with a sofa and dining table"></div>
    <div class="price">$150</div>
    <div class="card-title">Brand New Luxury Living<br>Stunning Contemporary Design</div>
    <svg class="stars" width="90" height="14" viewBox="0 0 90 14"><use href="#st"/><use href="#st" x="18"/><use href="#st" x="36"/><use href="#st" x="54"/><path transform="translate(72)" d="M7 0l2 5h5l-4 3 1.6 5L7 10l-4.6 3L4 8 0 5h5z" fill="#fff"/></svg>
    <p class="card-text">Lorem ipsum dolor sit amet, consectetur adipi-<br>scing elit</p>
    <div class="card-meta">1 Bedroom, Max 4 people</div>
    <div class="btn-fill">DETAILS</div><div class="btn-line">BOOK NOW</div>
  </article>
  <article class="card" style="left:436px;top:50px">
    <div class="card-photo photo-b" role="img" aria-label="Photo of a white minimal room with a floor lamp"></div>
    <div class="ribbon">Best Offer</div>
    <div class="price">$150</div>
    <div class="card-title">Brand New Luxury Living<br>Stunning Contemporary Design</div>
    <svg class="stars" width="90" height="14" viewBox="0 0 90 14"><use href="#st"/><use href="#st" x="18"/><use href="#st" x="36"/><use href="#st" x="54"/><path transform="translate(72)" d="M7 0l2 5h5l-4 3 1.6 5L7 10l-4.6 3L4 8 0 5h5z" fill="#fff"/></svg>
    <p class="card-text">Lorem ipsum dolor sit amet, consectetur adipi-<br>scing elit</p>
    <div class="card-meta">1 Bedroom, Max 4 people</div>
    <div class="btn-fill">DETAILS</div><div class="btn-line">BOOK NOW</div>
  </article>
  <article class="card" style="left:787px;top:50px">
    <div class="card-photo photo-c" role="img" aria-label="Photo of a study corner with shelves and a desk"></div>
    <div class="price">$150</div>
    <div class="card-title">Brand New Luxury Living<br>Stunning Contemporary Design</div>
    <svg class="stars" width="90" height="14" viewBox="0 0 90 14"><use href="#st"/><use href="#st" x="18"/><use href="#st" x="36"/><use href="#st" x="54"/><path transform="translate(72)" d="M7 0l2 5h5l-4 3 1.6 5L7 10l-4.6 3L4 8 0 5h5z" fill="#fff"/></svg>
    <p class="card-text">Lorem ipsum dolor sit amet, consectetur adipi-<br>scing elit</p>
    <div class="card-meta">1 Bedroom, Max 4 people</div>
    <div class="btn-fill">DETAILS</div><div class="btn-line">BOOK NOW</div>
  </article>

  <article class="card" style="left:86px;top:524px">
    <div class="card-photo photo-a" role="img" aria-label="Photo of a bright living room with a sofa and dining table"></div>
    <div class="price">$150</div>
    <div class="card-title">Brand New Luxury Living<br>Stunning Contemporary Design</div>
    <svg class="stars" width="90" height="14" viewBox="0 0 90 14"><use href="#st"/><use href="#st" x="18"/><use href="#st" x="36"/><use href="#st" x="54"/><path transform="translate(72)" d="M7 0l2 5h5l-4 3 1.6 5L7 10l-4.6 3L4 8 0 5h5z" fill="#fff"/></svg>
    <p class="card-text">Lorem ipsum dolor sit amet, consectetur adipi-<br>scing elit</p>
    <div class="card-meta">1 Bedroom, Max 4 people</div>
    <div class="btn-fill">DETAILS</div><div class="btn-line">BOOK NOW</div>
  </article>
  <article class="card" style="left:436px;top:524px">
    <div class="card-photo photo-b" role="img" aria-label="Photo of a white minimal room with a floor lamp"></div>
    <div class="ribbon">Best Offer</div>
    <div class="price">$150</div>
    <div class="card-title">Brand New Luxury Living<br>Stunning Contemporary Design</div>
    <svg class="stars" width="90" height="14" viewBox="0 0 90 14"><use href="#st"/><use href="#st" x="18"/><use href="#st" x="36"/><use href="#st" x="54"/><path transform="translate(72)" d="M7 0l2 5h5l-4 3 1.6 5L7 10l-4.6 3L4 8 0 5h5z" fill="#fff"/></svg>
    <p class="card-text">Lorem ipsum dolor sit amet, consectetur adipi-<br>scing elit</p>
    <div class="card-meta">1 Bedroom, Max 4 people</div>
    <div class="btn-fill">DETAILS</div><div class="btn-line">BOOK NOW</div>
  </article>
  <article class="card" style="left:787px;top:524px">
    <div class="card-photo photo-c" role="img" aria-label="Photo of a study corner with shelves and a desk"></div>
    <div class="price">$150</div>
    <div class="card-title">Brand New Luxury Living<br>Stunning Contemporary Design</div>
    <svg class="stars" width="90" height="14" viewBox="0 0 90 14"><use href="#st"/><use href="#st" x="18"/><use href="#st" x="36"/><use href="#st" x="54"/><path transform="translate(72)" d="M7 0l2 5h5l-4 3 1.6 5L7 10l-4.6 3L4 8 0 5h5z" fill="#fff"/></svg>
    <p class="card-text">Lorem ipsum dolor sit amet, consectetur adipi-<br>scing elit</p>
    <div class="card-meta">1 Bedroom, Max 4 people</div>
    <div class="btn-fill">DETAILS</div><div class="btn-line">BOOK NOW</div>
  </article>
</section>

<section class="interior">
  <h2 class="section-title script" style="top:1978px">Interior Designed</h2>
  <div class="kicker abs" style="left:0;top:2026px;width:1200px">BY LUMEN</div>
  <p class="interior-text">Lorem ipsum dolor sit amet, consectetur adipiscing elit, sed do eiusmod tempor incididunt ut labore et dolore magna aliqua. Ut enim ad minim veniam, quis nostrud exercitation ullamco laboris nisi ut aliquip ex ea commodo consequat. Duis aute irure dolor in reprehenderit in voluptate velit esse cillum dolore eu fugiat nulla pariatur. Excepteur sint occaecat cupidatat non proident, sunt in culpa qui officia deserunt mollit anim id est laborum.</p>

  <div class="tile" style="left:86px;top:2188px;width:335px;height:250px;background:linear-gradient(160deg,#e6e2dc,#cfc7bc 55%,#8e8478)" role="img" aria-label="Photo of a bedroom with a pendant lamp and desk"></div>
  <div class="tile" style="left:86px;top:2448px;width:335px;height:426px;background:linear-gradient(160deg,#f4f3f1,#dcd8d2 50%,#8c857c)" role="img" aria-label="Photo of a lounge with a grey sofa and cushions"></div>
  <div class="tile" style="left:431px;top:2188px;width:333px;height:373px;background:linear-gradient(160deg,#6b6b70,#3b3b40 60%,#26262b)" role="img" aria-label="Photo of a white partition wall dividing a room">
    <div class="zoom" style="left:140px;top:160px"><svg width="52" height="52" viewBox="0 0 52 52"><circle cx="25" cy="25" r="6" fill="none" stroke="#222" stroke-width="2.5"/><line x1="29.5" y1="29.5" x2="33" y2="33" stroke="#222" stroke-width="2.5"/></svg></div>
  </div>
  <div class="tile" style="left:431px;top:2571px;width:333px;height:303px;background:linear-gradient(170deg,#7a4f28,#b07a45 50%,#d9a56a)" role="img" aria-label="Photo of a warm wooden dining area with cabinets"></div>
  <div class="tile" style="left:774px;top:2188px;width:335px;height:303px;background:linear-gradient(160deg,#cfc4b6,#b9a895 55%,#c48a4a)" role="img" aria-label="Photo of a living room with an orange sofa and painting"></div>
  <div class="tile" style="left:774px;top:2501px;width:335px;height:373px;background:linear-gradient(160deg,#f1ede6,#e0d7cb 55%,#b59d86)" role="img" aria-label="Photo of a bright room with curtains and a globe lamp"></div>
</section>

<section class="reminders">
  <h2 class="section-title script" style="top:2944px">Important Reminders</h2>
  <div class="kicker abs" style="left:0;top:2990px;width:1200px">NEED TO KNOW</div>

  <div class="reminder" style="left:248px">
    <svg width="60" height="60" viewBox="0 0 60 60" fill="none" stroke="#c9a54b" stroke-width="2"><path d="M8 24L30 8l22 16"/><rect x="13" y="22" width="34" height="32"/><rect x="19" y="28" width="6" height="6"/><rect x="35" y="28" width="6" height="6"/><rect x="19" y="39" width="6" height="6"/><rect x="35" y="39" width="6" height="6"/><rect x="27" y="44" width="6" height="10"/></svg>
    <p>Also available to rent all the apart-<br>ments together for companies or<br>larger groups</p>
  </div>
  <div class="reminder" style="left:480px">
    <svg width="60" height="60" viewBox="0 0 60 60" fill="none" stroke="#c9a54b" stroke-width="2"><circle cx="30" cy="32" r="22"/><line x1="30" y1="5" x2="30" y2="10"/><line x1="25" y1="5" x2="35" y2="5"/><path d="M30 20v12l-8 8"/></svg>
    <p>12 noon; earliest check in 3pm<br>both are flexible by arrangement</p>
  </div>
  <div class="reminder" style="left:712px">
    <svg width="60" height="60" viewBox="0 0 60 60" fill="none" stroke="#c9a54b" stroke-width="2"><circle cx="30" cy="30" r="24"/><path d="M37 21c-2-3-14-4-14 3s14 4 14 11-12 6-15 2"/><line x1="30" y1="14" x2="30" y2="46"/></svg>
    <p>Prices from 150 USD per night<br>including tax</p>
  </div>
</section>

<footer class="footer">
  <p class="about">Vivamus viverra, ligula non tincidunt pulvinar, augue est sagittis leo, id feugiat enim lorem quis nisl. Quisque ac eros egestas, convallis risus vitae, gravida enim.</p>
  <span class="read-more">Read More</span>

  <h4 style="left:362px">QUICK LINKS</h4>
  <ul class="links">
    <li>Home</li><li class="active">About Us</li><li>Services</li><li>Products</li><li>Latest News &amp; Blogs</li><li>Contact Us</li>
  </ul>

  <h4 style="left:612px">LATEST NEWS</h4>
  <div class="news" style="top:130px">
    <div class="thumb" style="background:linear-gradient(135deg,#d6d0c6,#8a8278)" role="img" aria-label="Blog post thumbnail of an apartment interior"></div>
    <div class="body"><b>YOUR TITLE BLOG HERE</b><br>Phasellus ut condimentum diam, eget tempus lorem.<br>21 December, 2017</div>
  </div>
  <div class="abs" style="left:612px;top:252px;width:240px;height:1px;background:#2a2f40"></div>
  <div class="news" style="top:272px">
    <div class="thumb" style="background:var(--gold)"><svg width="44" height="44" viewBox="0 0 44 44"><path d="M22 14v16M14 22h16" stroke="#fff" stroke-width="2.5"/></svg></div>
    <div class="body"><b>YOUR TITLE BLOG HERE</b><br>Phasellus ut condimentum diam, eget tempus lorem.<br>21 December, 2017</div>
  </div>

  <h4 style="left:912px">NEWS LETTER</h4>
  <div class="newsletter"><span>Your email here</span><i><svg width="36" height="38" viewBox="0 0 36 38"><path d="M15 14l6 5-6 5z" fill="#fff"/></svg></i></div>
  <h4 style="left:912px;top:212px;color:#fff">SOCIAL</h4>
  <div class="social-dot" style="left:912px"></div>
  <div class="social-dot" style="left:942px"></div>
  <div class="social-dot" style="left:972px"></div>
</footer>
<div class="bottom-bar">Lumen Copyright 2017</div>

</body>
</html>
```